Medical Internet Marketing Company Needs a Site!

We need a new, fresh website for our search engine optimization and social media marketing company. We specialize in helping medical practices, doctors, physicians, and hospitals with their online presence and web ranking. The site should lean towards being suited for these audiences.

We have several examples of website that we like as well as things that we like about them.

Here are sites that we enjoy.

www.brightwavelab.com

It's a good design for the site all around. The videos, buttons, and images are all excellent. They did a fine job.

- We really like their "contact us" side bar and want to include one like it on the secondary pages.

www.corvantis.net

- We don't like the "thickness" of the top navigation bar.
- We like the page colors, easy navigation, and big call to action phone number in the top right corner.

http://www.teluvo.com/

Out of all the examples provided, Teluvo is our favorite and closest look and style to what we are looking for.

- We really like the openness of the design, such as space between the text and background.

- We want a price page in a style very similar to their pricing page with the services listed and check-marks, etc. although we intend to have multiple service package columns much like Corvantis's SEO pricing page.

- The way the video fits into the home page header is very organized, simple, and attention grabbing. We intend to place a slider with videos here.

- We need a page design that will allow for an image slider like Teluvo's Features page.

Here's a great example of a medical internet marketing website: http://www.dermaplex.com/

Target Market(s)

Our target market is doctors, typically male and typically 40-45 years old. I

Industry/Entity Type

Marketing

Requirements
Must have
• The homepage should have a slider in the video. Interior pages should have a video in the very top similar to how they do it on www.brightwavelab.com

The top navigation tabs needed are:
- Home
- Solutions
- Resources
- About
- Why Quelvo
- Contact

The sidebar should have a GREAT call to action in it on interior pages.

There should be one interior page that is similar to this - http://www.teluvo.com/pricing/

There needs to be a page with multiple boxes that take up a row of the web page's body. This page will house all the case studies similar to brightwave lab's: http://www.brightwavelab.com/success-stories/case-studies/ The one exception is we want the case studies to be inside of "boxes" instead of between horizontal lines like brightwave lab's.
Nice to have
• Color, professional, and clean. GREAT use of calls to actions.

```html
<!DOCTYPE html>
<html lang="en">
<head>
<meta charset="utf-8">
<title>Quelvo – Medical Internet Marketing</title>
<link href="https://fonts.googleapis.com/css2?family=Open+Sans:ital,wght@0,400;0,600;0,700;1,700&display=swap" rel="stylesheet">
<style>
:root{
  --blue:#1f7fc6;
  --blue-dark:#125e98;
  --blue-deep:#0d4c7e;
  --blue-pale:#e6f2fb;
  --green:#7cc142;
  --green-dark:#5a9a2a;
  --orange:#f07c1e;
  --ink:#333b44;
  --muted:#6d7782;
  --page:#eef2f5;
  --white:#ffffff;
}
*{box-sizing:border-box;margin:0;padding:0}
html,body{width:805px;height:1200px;overflow:hidden}
body{background:var(--page);font-family:"Open Sans",Arial,sans-serif;color:var(--ink);position:relative;font-size:9px;line-height:1.45}
.abs{position:absolute}

.site-header{left:0;top:0;width:805px;height:64px;background:linear-gradient(#2a8ed4,var(--blue-dark))}
.brand{left:38px;top:9px;display:flex;align-items:center;gap:8px}
.brand-mark{width:18px;height:18px;background:var(--white);border-radius:50%}
.brand-name{color:var(--white);font-weight:700;font-size:22px;letter-spacing:1px}
.call{right:38px;top:10px;color:var(--white);font-weight:700;font-size:16px}
.main-nav{left:35px;top:42px;width:735px;height:22px;display:flex;background:var(--blue-deep)}
.main-nav a{flex:1;color:var(--white);text-decoration:none;font-size:10px;font-weight:600;text-align:center;line-height:22px;border-right:1px solid rgba(255,255,255,.2)}
.main-nav a:last-child{border-right:0}

.feedback-tab{left:0;top:180px;width:18px;height:80px;background:var(--green);color:var(--white);font-size:8px;font-weight:700;writing-mode:vertical-rl;transform:rotate(180deg);text-align:center;line-height:18px;border-radius:0 3px 3px 0}

.hero{left:35px;top:72px;width:735px;height:250px;background:var(--white);box-shadow:0 1px 4px rgba(0,0,0,.2)}
.hero-video{left:6px;top:6px;width:508px;height:194px;background:radial-gradient(ellipse at 55% 30%,#8fa4b8,#3b4b5c 55%,#1d2731)}
.play{left:239px;top:82px}
.hero-thumbs{left:6px;top:202px;width:508px;height:42px;background:#222c35;display:flex;gap:6px;padding:5px 8px}
.hero-thumbs span{flex:1;background:linear-gradient(#56687a,#34414e)}
.hero-pitch{left:518px;top:6px;width:211px;height:238px;background:var(--green);color:var(--white);padding:12px 12px}
.hero-pitch h2{font-size:12px;font-weight:700;line-height:1.3;margin-bottom:12px}
.hero-pitch ul{list-style:none}
.hero-pitch li{display:flex;gap:7px;font-size:9.5px;margin-bottom:10px;line-height:1.3}
.hero-pitch li svg{flex:none;margin-top:1px}

.features{left:35px;top:335px;width:735px;display:flex}
.feature{flex:1;padding:0 14px}
.feature-head{display:flex;gap:7px;align-items:flex-start}
.num{flex:none;width:22px;height:22px;border-radius:50%;background:var(--blue);color:var(--white);font-weight:700;font-size:12px;text-align:center;line-height:22px}
.feature h3{font-size:12px;color:var(--blue-dark);line-height:1.2;font-weight:600}
.feature p{color:var(--muted);font-size:7.5px;margin:4px 0 0 29px}
.feature-art{width:100px;height:100px;border-radius:50%;margin:10px auto 0;background:radial-gradient(circle at 40% 35%,#ffffff,#c9dbe9 70%,#a9c1d4)}

.cta-row{left:35px;top:545px;width:735px;height:44px;display:flex;align-items:center;gap:18px;padding-left:45px}
.get-started{color:var(--blue);font-style:italic;font-weight:700;font-size:14px;display:flex;align-items:center;gap:8px}
.btn{display:block;width:180px;height:30px;color:var(--white);font-size:10px;font-weight:700;padding:4px 10px;line-height:1.15;border-radius:2px}
.btn small{display:block;font-size:6.5px;font-weight:400}
.btn-blue{background:var(--blue-dark)}
.btn-orange{background:var(--orange)}

.services{left:45px;top:620px;width:340px;height:265px;background:var(--blue-pale);border:1px solid #c2daed;padding:14px 16px}
.services h3,.news h3{font-size:12px;color:var(--blue-dark);font-weight:600;margin-bottom:8px}
.services p{font-size:7.5px;color:var(--muted);margin-bottom:3px}
.news{left:410px;top:620px;width:350px;height:265px;padding:14px 0}
.news p{font-size:7.5px;color:var(--muted);margin-bottom:8px}
.subscribe{display:flex;gap:6px;margin-top:6px}
.subscribe span{display:block;width:180px;height:18px;border:1px solid #c9d2da;background:var(--white);font-size:7px;color:#9aa3ac;padding:3px 6px}
.subscribe b{display:block;width:70px;height:18px;background:var(--blue);color:var(--white);font-size:8px;text-align:center;line-height:18px}

.signup{left:305px;top:912px;width:195px;height:34px;background:var(--green);border:2px solid var(--green-dark);color:var(--blue-deep);font-weight:700;font-size:14px;text-align:center;line-height:30px;border-radius:3px}

.site-footer{left:35px;top:975px;width:735px;height:225px;background:var(--blue)}
.footer-cols{display:flex;padding:10px 14px 0;height:118px}
.footer-col{flex:1;color:var(--white)}
.footer-col h4{font-size:10px;font-weight:600;margin-bottom:5px}
.footer-col p{font-size:6.5px;line-height:1.5;opacity:.9}
.social{display:grid;grid-template-columns:repeat(2,14px);gap:5px}
.social span{width:14px;height:14px;background:var(--white);border-radius:2px;opacity:.85}
.markets{background:var(--blue-deep);margin:0 8px;height:74px;padding:6px 8px;color:var(--white)}
.markets h4{font-size:7px;font-weight:600;margin-bottom:3px}
.markets-grid{display:grid;grid-template-columns:repeat(7,1fr);font-size:6px;line-height:1.5;opacity:.9}
.copyright{font-size:6px;color:var(--white);padding:6px 14px;opacity:.85}
</style>
</head>
<body>
<header class="abs site-header">
  <div class="abs brand"><span class="brand-mark"></span><span class="brand-name">Quelvo</span></div>
  <div class="abs call">Call (940) 555-0172</div>
  <nav class="abs main-nav">
    <a href="#">Home</a><a href="#">Solutions</a><a href="#">Resources</a><a href="#">About</a><a href="#">Why Quelvo</a><a href="#">Contact</a>
  </nav>
</header>

<div class="abs feedback-tab">Feedback</div>

<section class="abs hero">
  <div class="abs hero-video" role="img" aria-label="Video still of a speaker addressing a seated audience in a conference hall">
    <svg class="abs play" width="30" height="30" viewBox="0 0 30 30"><circle cx="15" cy="15" r="14" fill="rgba(255,255,255,.8)"/><path d="M12 9l9 6-9 6z" fill="#1d2731"/></svg>
  </div>
  <div class="abs hero-thumbs" role="img" aria-label="Row of video slide thumbnails"><span></span><span></span><span></span><span></span><span></span><span></span></div>
  <div class="abs hero-pitch">
    <h2>Quelvo is a national medical Internet-marketing group.</h2>
    <ul>
      <li><svg width="10" height="10" viewBox="0 0 10 10"><path d="M1 5l3 3 5-6" stroke="#fff" stroke-width="1.8" fill="none"/></svg>We EMPOWER doctors nationwide</li>
      <li><svg width="10" height="10" viewBox="0 0 10 10"><path d="M1 5l3 3 5-6" stroke="#fff" stroke-width="1.8" fill="none"/></svg>We BUILD their practices</li>
      <li><svg width="10" height="10" viewBox="0 0 10 10"><path d="M1 5l3 3 5-6" stroke="#fff" stroke-width="1.8" fill="none"/></svg>Highly specialized PATIENT ENGAGEMENT strategies</li>
      <li><svg width="10" height="10" viewBox="0 0 10 10"><path d="M1 5l3 3 5-6" stroke="#fff" stroke-width="1.8" fill="none"/></svg>Designed to bring in REAL PATIENTS</li>
    </ul>
  </div>
</section>

<section class="abs features">
  <div class="feature">
    <div class="feature-head"><span class="num">1</span><h3>Search Engine Optimization</h3></div>
    <p>Be found on the first page of search results where patients look for care in your area.</p>
    <div class="feature-art" role="img" aria-label="Illustration of a globe with a search magnifier"></div>
  </div>
  <div class="feature">
    <div class="feature-head"><span class="num">2</span><h3>Pay Per Click Advertising</h3></div>
    <p>We use targeted pay-per-click campaigns to drive new patients straight to your office.</p>
    <div class="feature-art" role="img" aria-label="Illustration of a computer mouse"></div>
  </div>
  <div class="feature">
    <div class="feature-head"><span class="num">3</span><h3>Strategic Consulting</h3></div>
    <p>Through hard work and a lot of heart we bring clarity to every strategic plan.</p>
    <div class="feature-art" role="img" aria-label="Illustration of a strategy board with chess pieces"></div>
  </div>
</section>

<div class="abs cta-row">
  <div class="get-started">Get Started!<svg width="40" height="10" viewBox="0 0 40 10"><path d="M0 5h36M31 1l5 4-5 4" stroke="#1f7fc6" stroke-width="1.5" fill="none"/></svg></div>
  <a class="btn btn-blue">Lorem ipsum dolor<small>Sed ut perspiciatis unde omnis iste</small></a>
  <a class="btn btn-orange">Lorem ipsum dolor<small>Sed ut perspiciatis unde omnis iste</small></a>
</div>

<section class="abs services">
  <h3>SEO &amp; Internet Marketing Services</h3>
  <p>What do we actually do, you ask?</p>
  <p>Funny you should ask.</p>
  <p>Fact: 93% of all Internet activity begins with a search engine query.</p>
  <p>Our work is to get your practice in front of those searches.</p>
  <p>Here's where we do this with proven methods for doctors.</p>
  <p>We help create a reason for new patients to call you today.</p>
  <p>How do we do this, you ask?</p>
  <p>We do this through building your site with care and focus.</p>
  <p>We help practices grow their reach and their patient lists.</p>
</section>

<section class="abs news">
  <h3>Latest Quelvo News</h3>
  <p>Lorem ipsum dolor sit amet, consectetur adipiscing elit.</p>
  <p>Donec rhoncus orci et amet nulla varius ut amet sodales nulla mauris.</p>
  <p>Ut ac nisl sed mauris laoreet sodales.</p>
  <div class="subscribe"><span>Enter your email address...</span><b>SUBSCRIBE</b></div>
</section>

<a class="abs signup">SIGN UP FOR FREE</a>

<footer class="abs site-footer">
  <div class="footer-cols">
    <div class="footer-col"><h4>Web Design</h4><p>Patient Education<br>Custom Video<br>Mobile</p></div>
    <div class="footer-col"><h4>Local Marketing</h4><p>Maps &amp; Reviews<br>Optimization<br>Search Marketing<br>SEO<br>PPC<br>Social Media &amp; Blogs<br>Reputation</p></div>
    <div class="footer-col"><h4>Pricing &amp; Samples</h4><p>How it Works<br>SEO<br>PPC<br>Social Media &amp; Blogs<br>Maps &amp; Reviews<br>Optimization</p></div>
    <div class="footer-col"><h4>Get Social</h4><div class="social"><span></span><span></span><span></span><span></span><span></span><span></span></div></div>
    <div class="footer-col"><h4>Contact</h4><p>QUELVO HEADQUARTERS<br>1200 Harbor Avenue<br>Suite 300, Dallas, TX<br>Phone: (940) 555-0172<br>Fax: (940) 555-0173<br>info@quelvo.com</p></div>
  </div>
  <div class="markets">
    <h4>Medical Markets</h4>
    <div class="markets-grid">
      <span>Plastic Surgeons</span><span>Bariatrics</span><span>Orthopedics</span><span>Chiropractic</span><span>Gastroenterology</span><span>Podiatry</span><span>Oncology</span>
      <span>Dental</span><span>Dermatology</span><span>Ophthalmology</span><span>Spine</span><span>Neurology</span><span>Pediatrics</span><span>Urology</span>
      <span>Cosmetic Dental</span><span>Fertility</span><span>Cardiology</span><span>ENT</span><span>OB-GYN</span><span>Physical Therapy</span><span>Vascular</span>
    </div>
  </div>
  <div class="copyright">Copyright © 2013 Quelvo. All rights reserved.</div>
</footer>
</body>
</html>
```